Folder Cover Design

We need a design for an A5 size folder cover into which a variable number of different A5 sheets can be placed. We are a health provision company in the UK providing therapy services to the PCB. These folders will contain essential information for patients after assessment including their treatment plan, results of diagnostics, advice for self-management etc..
We offer a high quality and very patient centred service, offering private health values to PCB patients, flexible and approachable, different from the normal over-bureaucratic services. Something different that people will want to keep. We will want to use our Logo and the PCB logo (which we are authorised to use. There are strict criteria around the blue PCB logo, mainly that if it is on the same page as other logos it must be top right, be in clear space and bigger by 1/3. Should project trust with a different approach, fresh & healthy..

Target Market(s)

All patients refered by their GP to our services in all areas..from Richmond to Margate.

Industry/Entity Type

Health

Requirements
Must have
• PCB Logo (White in Blue)
Vitalmore Logo (see www.vitalmore-example.org.uk)
'Working in partnership with the PCB'
'Your Health, Your Care'
'Community Clinics' (back cover?)
web address (back cover?)

```html
<!DOCTYPE html>
<html lang="en">
<head>
<meta charset="utf-8">
<title>Your Health Your Care – Vitalmore Folder Cover</title>
<link rel="stylesheet" href="https://fonts.googleapis.com/css2?family=Arimo:wght@400;700&display=swap">
<style>
  :root {
    --paper: #ffffff;
    --leaf-deep: #2f4a1c;
    --leaf-mid: #5f8a2e;
    --leaf-light: #a9c85a;
    --brand-green: #3f8a2c;
    --tagline-green: #7bb22a;
    --band-1: #1d2a18;
    --band-2: #3c5a2a;
    --band-3: #8cb33f;
    --band-4: #c3d92f;
    --band-5: #b6c25b;
  }
  * { margin: 0; padding: 0; box-sizing: border-box; }
  html, body {
    width: 847px;
    height: 1200px;
    overflow: hidden;
    background: var(--paper);
  }
  .cover {
    position: relative;
    width: 847px;
    height: 1200px;
    background: var(--paper);
    font-family: "Arimo", Arial, sans-serif;
  }
  .headline {
    position: absolute;
    top: 318px;
    left: 0;
    width: 100%;
    text-align: center;
    font-weight: 700;
    font-size: 128px;
    line-height: 136px;
    letter-spacing: -5px;
    background: linear-gradient(160deg, var(--leaf-light) 0%, var(--leaf-mid) 35%, var(--leaf-deep) 60%, var(--leaf-mid) 80%, var(--leaf-light) 100%);
    -webkit-background-clip: text;
    background-clip: text;
    color: transparent;
  }
  .headline span { display: block; }
  .brand {
    position: absolute;
    right: 20px;
    top: 1026px;
    display: flex;
    align-items: center;
    gap: 12px;
  }
  .brand-dot {
    width: 62px;
    height: 62px;
    border-radius: 50%;
    background: var(--brand-green);
  }
  .brand-name {
    font-weight: 700;
    font-size: 54px;
    letter-spacing: -1px;
    color: var(--brand-green);
  }
  .partnership {
    position: absolute;
    right: 20px;
    top: 1126px;
    font-size: 20px;
    color: var(--tagline-green);
  }
  .colour-band {
    position: absolute;
    left: 0;
    bottom: 0;
    width: 100%;
    height: 30px;
    display: flex;
  }
  .colour-band i { flex: 1; }
  .colour-band i:nth-child(1) { background: var(--band-1); }
  .colour-band i:nth-child(2) { background: var(--band-2); }
  .colour-band i:nth-child(3) { background: var(--band-3); }
  .colour-band i:nth-child(4) { background: var(--band-4); }
  .colour-band i:nth-child(5) { background: var(--band-5); }
</style>
</head>
<body>
  <main class="cover">
    <h1 class="headline" role="img" aria-label="Your Health Your Care, lettering filled with a close-up photograph of green grass">
      <span>Your Health</span>
      <span>Your Care</span>
    </h1>

    <div class="brand">
      <span class="brand-dot"></span>
      <span class="brand-name">Vitalmore</span>
    </div>
    <p class="partnership">Working in partnership with the PCB</p>

    <div class="colour-band" aria-hidden="true">
      <i></i><i></i><i></i><i></i><i></i>
    </div>
  </main>
</body>
</html>
```